Business card design needed

Family General Practitioner/ Family Physician.
Logo is the logo of the Crestmoor Guild of Family Clinicians Australia
http://kvplm.tarevo.edu.au/PictureGallery/logos/pages/CGFC%20logo_jpg.htm

Reason: Just a bit more time to make changes and the weekend for me to look at things closely and to choose. Thanks, Lumi

Thanks for all the submissions. So many of them are really works of art. Not one of them are not good. The ones that I am eliminating are the ones that I think are not suitable for me personally only, and because if I don't, it makes it very difficult to decide as many of you are also sending me slight variations of a card. I have just decided to choose a second place card too. Can't thank you all enough. Good luck, Lumi. P.S - Working today till 10 pm as the card says :-), so probably won't be able to give a feedback till late Saturday night or Sunday morning here in Sydney, Australia. 

Reason: Just added a second place to the budget and realised that Australia is ahead of the rest of the world in the time zone (only :-) - don't want to offend anyone or start a debate!! ) , so Monday deadline will mean it will be a weekend for the rest of the world. Just wanted to give everyone more time to submit their best, especially since I will be picking a second card too. Can't thank everyone enough for the submissions. P.S - Not keen on photos on the card.

Contact Information for Business Card

Dr. Lumi Harcourt M.B.B.S., F.C.G.F.C
Family General Practitioner
Address, timings, phone and fax number on the back.

Requirements
Must have
• Timings
Mon 7 am - 7 pm
Tues 7 am - 12 pm
Wed 7 am - 10 pm
Thurs 7 am - 12 pm
Fri 7 am - 8 pm
Sat 8 am - 10 pm
Sun - Off

```html
<!DOCTYPE html>
<html lang="en">
<head>
<meta charset="utf-8">
<title>Dr. Lumi Harcourt – Business Card</title>
<link rel="stylesheet" href="https://fonts.googleapis.com/css2?family=PT+Sans:wght@400;700&family=Roboto+Condensed:wght@700&family=Noto+Serif:wght@700&display=swap">
<style>
  :root {
    --backdrop: #ece7df;
    --card-grey: #4a4a4a;
    --card-white: #ffffff;
    --ink-light: #ffffff;
    --ink-dark: #2f2f2f;
    --rule: #8a8a8a;
  }
  html, body {
    margin: 0;
    padding: 0;
    overflow: hidden;
  }
  body {
    width: 1200px;
    height: 368px;
    background: var(--backdrop);
    position: relative;
  }
  .card {
    position: absolute;
    top: 33px;
    width: 525px;
    height: 300px;
    background: var(--card-grey);
    overflow: hidden;
  }
  .card--front { left: 36px; }
  .card--back { left: 621px; }

  /* Front */
  .guild-mark {
    position: absolute;
    left: 66px;
    top: 129px;
    display: flex;
    align-items: center;
    gap: 8px;
    font-family: "PT Sans", sans-serif;
    font-weight: 700;
    font-size: 20px;
    color: var(--ink-light);
    letter-spacing: 1px;
  }
  .guild-mark__dot {
    width: 14px;
    height: 14px;
    border-radius: 50%;
    background: var(--ink-light);
  }
  .identity {
    position: absolute;
    left: 190px;
    width: 305px;
    text-align: center;
    font-family: "PT Sans", sans-serif;
    color: var(--ink-light);
  }
  .identity__name {
    position: absolute;
    top: 76px;
    left: 0;
    width: 100%;
    margin: 0;
    font-weight: 400;
    font-size: 31px;
    letter-spacing: -0.3px;
  }
  .identity__credentials {
    position: absolute;
    top: 132px;
    left: 0;
    width: 100%;
    margin: 0;
    font-size: 12px;
  }
  .identity__role {
    position: absolute;
    top: 185px;
    left: 0;
    width: 100%;
    margin: 0;
    font-weight: 700;
    font-size: 16px;
  }
  .stripes {
    position: absolute;
    left: 0;
    top: 264px;
    width: 100%;
    height: 20px;
  }

  /* Back */
  .hours {
    position: absolute;
    top: 0;
    left: 0;
    width: 100%;
    height: 172px;
    color: var(--ink-light);
  }
  .hours__title {
    position: absolute;
    top: 16px;
    left: 0;
    width: 100%;
    margin: 0;
    text-align: center;
    font-family: "Noto Serif", serif;
    font-weight: 700;
    font-size: 14px;
    letter-spacing: -0.2px;
  }
  .hours__table {
    position: absolute;
    top: 47px;
    left: 177px;
    border-collapse: collapse;
    font-family: "Roboto Condensed", sans-serif;
    font-weight: 700;
    font-size: 12.5px;
  }
  .hours__table td {
    padding: 0;
    height: 15.8px;
    line-height: 15.8px;
  }
  .hours__day { width: 79px; }
  .hours__sep { width: 20px; }
  .contact {
    position: absolute;
    left: 0;
    top: 172px;
    width: 100%;
    height: 128px;
    background: var(--card-white);
    font-family: "Roboto Condensed", sans-serif;
    font-weight: 700;
    font-size: 12.5px;
    color: var(--ink-dark);
  }
  .contact__address {
    position: absolute;
    left: 110px;
    top: 39px;
    margin: 0;
    font-style: normal;
    line-height: 20.5px;
  }
  .contact__divider {
    position: absolute;
    left: 309px;
    top: 37px;
    width: 1px;
    height: 59px;
    background: var(--rule);
  }
  .contact__lines {
    position: absolute;
    left: 330px;
    top: 50px;
    margin: 0;
    padding: 0;
    list-style: none;
    line-height: 21px;
  }
</style>
</head>
<body>
  <section class="card card--front">
    <div class="guild-mark" aria-label="Crestmoor Guild of Family Clinicians Australia">
      <span class="guild-mark__dot"></span>CGFC
    </div>
    <div class="identity">
      <h1 class="identity__name">Dr. Lumi Harcourt</h1>
      <p class="identity__credentials">M.B.B.S., F.C.G.F.C</p>
      <p class="identity__role">Family General Practitioner</p>
    </div>
    <svg class="stripes" viewBox="0 0 525 20" preserveAspectRatio="none" aria-hidden="true">
      <rect x="0" y="0" width="525" height="3" fill="#ffffff"/>
      <rect x="0" y="7" width="525" height="3" fill="#ffffff"/>
      <rect x="0" y="14" width="525" height="3" fill="#ffffff"/>
    </svg>
  </section>

  <section class="card card--back">
    <div class="hours">
      <h2 class="hours__title">Working Hours</h2>
      <table class="hours__table">
        <tr><td class="hours__day">Monday</td><td class="hours__sep">:</td><td>7 AM -&nbsp; 7 PM</td></tr>
        <tr><td class="hours__day">Tuesday</td><td class="hours__sep">:</td><td>7 AM - 12 PM</td></tr>
        <tr><td class="hours__day">Wednesday</td><td class="hours__sep">:</td><td>7 AM - 10 PM</td></tr>
        <tr><td class="hours__day">Thursday</td><td class="hours__sep">:</td><td>7 AM - 12 PM</td></tr>
        <tr><td class="hours__day">Friday</td><td class="hours__sep">:</td><td>7 AM -&nbsp; 8 PM</td></tr>
        <tr><td class="hours__day">Saturday</td><td class="hours__sep">:</td><td>8 AM - 10 PM</td></tr>
        <tr><td class="hours__day">Sunday</td><td class="hours__sep">:</td><td>OFF</td></tr>
      </table>
    </div>
    <div class="contact">
      <address class="contact__address">
        Upper Level, Harbour Court,<br>
        Elmwood Square Shopping Centre,<br>
        Elmwood Hill, NSW 2761
      </address>
      <div class="contact__divider"></div>
      <ul class="contact__lines">
        <li>P : 02 5550 1840</li>
        <li>F : 02 5550 1877</li>
      </ul>
    </div>
  </section>
</body>
</html>
```